lifestyle website Dubai

I need to create a lifestyle website homepage design,

The top nav menu will be:
- Home
- UAE Life
- Emirates Insider
- Career Corner
- HR Essentials
- Blog Beat
- Connect with us

the homepage contents sections will be something like:

- Top Beach Clubs
- Nightlife & Eats
- Outdoor Thrills
- Shopping Spree
- Staycays
- Explore

I've attached an example for the design - but this is not my design so don't copy it.. If you could imagine an Azurio holiday - Thats the look and feel im after.

```html
<!DOCTYPE html>
<html lang="en">
<head>
<meta charset="utf-8">
<title>Sunvista Dubai</title>
<link href="https://fonts.googleapis.com/css2?family=Montserrat:wght@800;900&family=Poppins:wght@400;500;600;700;800&display=swap" rel="stylesheet">
<style>
:root{
  --ink:#141414;
  --ink-deep:#0c0c0c;
  --mint:#14c984;
  --mint-bright:#1de39a;
  --mint-dark:#0fae72;
  --violet:#6a3be0;
  --lime:#d7f23a;
  --white:#ffffff;
  --muted:#bdbdbd;
  --footer:#1d2b2a;
}
*{margin:0;padding:0;box-sizing:border-box}
html,body{width:1200px;height:4026px;overflow:hidden;background:var(--ink)}
body{position:relative;font-family:"Poppins",sans-serif;color:var(--white)}
.abs{position:absolute}
.brand{font-family:"Poppins",sans-serif;font-weight:700;color:var(--mint-bright);font-size:24px;letter-spacing:1px}
.social{display:flex;gap:12px}
.social span{width:27px;height:27px;border:1.5px solid var(--mint);border-radius:50%;display:block}
.pill{display:inline-flex;align-items:center;gap:6px;border-radius:20px;font-weight:600;font-size:11px;letter-spacing:1px;text-transform:uppercase}
.pill.solid{background:var(--mint-bright);color:var(--white)}
.pill.ghost{border:1.5px solid var(--mint);color:var(--mint)}
.pill svg{width:12px;height:12px}
.nav{display:flex;font-size:11px;font-weight:600;letter-spacing:1.2px;text-transform:uppercase}
.nav a{color:var(--white);text-decoration:none;position:absolute;transform:translateX(-50%);white-space:nowrap}
.nav a.active{color:var(--mint-bright);border-bottom:2px solid var(--mint-bright);padding-bottom:3px}
.hero{left:0;top:0;width:1200px;height:672px;background:linear-gradient(180deg,#0d0d0d 0%,#3a6aa8 12%,#86abd6 35%,#9ab7d4 52%,#3b5570 72%,#1e2a26 88%,var(--ink) 100%)}
.hero-title{top:268px;width:1200px;text-align:center;font-family:"Montserrat",sans-serif;font-weight:900;font-size:35px;letter-spacing:7px}
.hero-text{top:322px;width:1200px;text-align:center;font-size:13.5px;line-height:23px}
.eyebrow{font-size:17px;color:var(--muted);letter-spacing:.5px;text-transform:uppercase;padding-bottom:6px;border-bottom:1.5px solid #555}
.headline{font-family:"Montserrat",sans-serif;font-weight:900;font-size:54px;line-height:51px;letter-spacing:7px;text-transform:uppercase;-webkit-background-clip:text;background-clip:text;color:transparent}
.h-sea{background-image:linear-gradient(180deg,#9fc3d6,#d7b79a 60%,#f4efe7)}
.h-fire{background-image:linear-gradient(90deg,#ff4a1c,#ff8a2a 50%,#e2451d)}
.h-surf{background-image:linear-gradient(180deg,#7fd4e0,#2aa7c8 60%,#bfe9ee)}
.h-more{background-image:linear-gradient(90deg,#9fb6c2,#e0d6c6 50%,#8fa6b2)}
.body-text{font-size:13.5px;line-height:22.6px;color:#eaeaea}
.photo{position:absolute}
.card-name{position:absolute;left:16px;bottom:16px;font-weight:800;font-size:23px;line-height:25px;letter-spacing:1px;color:var(--white)}
.tile-tag{position:absolute;left:14px;bottom:10px;font-weight:700;font-size:13px;line-height:17px;letter-spacing:1px;text-transform:uppercase;color:var(--ink)}
.band{left:0;top:3066px;width:1200px;height:609px;background:var(--mint)}
.form-box{left:667px;top:3259px;width:353px;height:355px;background:var(--mint-dark)}
.field{position:absolute;left:36px;width:282px;border-bottom:1.5px solid #e9fff5;font-size:13px;letter-spacing:1px;padding-left:10px;padding-bottom:6px}
.contact-line{font-size:13.5px}
.contact-line b{font-weight:700}
.footer{left:0;top:3675px;width:1200px;height:351px;background:linear-gradient(180deg,#243433,#17211f)}
.foot-head{font-size:16px;letter-spacing:4px;text-transform:uppercase;text-align:center}
.foot-text{font-size:12.5px;line-height:19px;color:#9aa7a4;text-align:center}
</style>
</head>
<body>

<!-- hero -->
<div class="abs hero" role="img" aria-label="Dubai skyline with palm trees under a blue sky"></div>
<div class="abs" style="left:0;top:0;width:1200px;height:72px;background:linear-gradient(180deg,#0a0a0a,rgba(10,10,10,.85) 70%,rgba(10,10,10,0))"></div>
<div class="abs brand" style="left:187px;top:20px">Sunvista Dubai</div>
<div class="abs social" style="left:746px;top:23px"><span></span><span></span><span></span></div>
<div class="abs pill solid" style="left:866px;top:23px;width:154px;height:26px;justify-content:center">Connect with us
  <svg viewBox="0 0 12 12"><path d="M2 6h8M7 3l3 3-3 3" stroke="#fff" stroke-width="1.6" fill="none"/></svg></div>
<nav class="abs nav" style="left:0;top:96px;width:1200px">
  <a class="active" style="left:203px">Home</a>
  <a style="left:319px">UAE Life</a>
  <a style="left:469px">Emirates Insider</a>
  <a style="left:650px">Career Corner</a>
  <a style="left:825px">HR Essentials</a>
  <a style="left:981px">Blog Beat</a>
</nav>
<h1 class="abs hero-title">SUNVISTA DUBAI, UNFILTERED</h1>
<p class="abs hero-text">We're your insider guide to the city's most exclusive beach clubs,<br>hottest parties, and experiences you won't want to miss.</p>
<div class="abs pill solid" style="left:462px;top:388px;width:121px;height:27px;justify-content:center">Sign me up!
  <svg viewBox="0 0 12 12"><rect x="1" y="2.5" width="10" height="7" fill="none" stroke="#fff" stroke-width="1.3"/><path d="M1 2.5l5 4 5-4" fill="none" stroke="#fff" stroke-width="1.3"/></svg></div>
<div class="abs pill ghost" style="left:594px;top:388px;width:153px;height:27px;justify-content:center;opacity:.7">Watch the video
  <svg viewBox="0 0 12 12"><circle cx="6" cy="6" r="5" fill="none" stroke="currentColor" stroke-width="1.2"/><path d="M5 4l3 2-3 2z" fill="currentColor"/></svg></div>

<!-- beach clubs -->
<div class="abs eyebrow" style="left:188px;top:742px;width:240px">Top Beach Clubs</div>
<h2 class="abs headline h-sea" style="left:186px;top:784px">Beach<br>Vibes<br>Only</h2>
<p class="abs body-text" style="left:186px;top:951px;width:380px">Crystal-clear waters, premium cocktails, and the ultimate day party scene. Let's be real. You deserve a break from the everyday grind, and Dubai is calling your name. Imagine: Soaking up the sun at a premium beach club, dancing until dawn in a rooftop haven with breathtaking views, and experiencing the city's legendary nightlife scene like never before.</p>
<div class="abs pill ghost" style="left:186px;top:1133px;width:120px;height:28px;justify-content:center">Learn more
  <svg viewBox="0 0 12 12"><path d="M2 6h8M7 3l3 3-3 3" stroke="currentColor" stroke-width="1.6" fill="none"/></svg></div>
<div class="photo" style="left:630px;top:790px;width:418px;height:305px;background:#050505;transform:rotate(-2deg)"></div>
<div class="photo" role="img" aria-label="Infinity pool at sunset with palm trees" style="left:630px;top:788px;width:410px;height:300px;background:linear-gradient(180deg,#7d93c9,#e9a7a6 45%,#f2b27a 52%,#4aa0c7 70%,#2a7fb0);transform:rotate(2deg)"></div>

<!-- hotel strip -->
<div class="photo" role="img" aria-label="Beach bar terrace with palms" style="left:0;top:1244px;width:204px;height:278px;background:linear-gradient(180deg,#8fb3d2,#c9a56b 55%,#6b5a3e)"><div class="card-name" style="left:0">Coralline<br>Palm</div></div>
<div class="photo" role="img" aria-label="Thatched beach umbrellas by the sea" style="left:204px;top:1280px;width:260px;height:276px;background:linear-gradient(180deg,#c9b18a,#d9c7a6 40%,#8fb3c2 60%,#b59a74)"><div class="card-name">Mirela<br>Beach Resort</div></div>
<div class="photo" role="img" aria-label="Waterfront resort lit at dusk" style="left:464px;top:1244px;width:260px;height:312px;background:linear-gradient(180deg,#1b2f7a,#2d4a9c 45%,#c79a4a 65%,#1a2540)"><div class="card-name" style="bottom:60px">Lantern Bay<br>Dubai</div></div>
<div class="photo" role="img" aria-label="Rocky shore with white parasols" style="left:724px;top:1280px;width:260px;height:276px;background:linear-gradient(180deg,#8c8c8c,#d9d9d9 40%,#5a5a5a 65%,#9bb8c9)"><div class="card-name" style="left:22px">Roamstead<br>Downtown</div></div>
<div class="photo" role="img" aria-label="Straw parasol and loungers on a sandy beach" style="left:984px;top:1244px;width:216px;height:278px;background:linear-gradient(180deg,#2f8fd6,#7cc3ec 45%,#a57a45 60%,#e9dcc4)"><div class="card-name">Solacia<br>Hotel Dubai</div></div>

<!-- nightlife -->
<div class="photo" style="left:163px;top:1734px;width:395px;height:282px;background:var(--mint-bright);transform:rotate(-2deg)"></div>
<div class="photo" role="img" aria-label="Friends in masks celebrating at a party" style="left:168px;top:1736px;width:390px;height:278px;background:linear-gradient(135deg,#e0244e,#7a1a8a 55%,#2a1a6a);transform:rotate(1deg)"></div>
<div class="abs eyebrow" style="left:644px;top:1678px;width:240px">Nightlife &amp; Eats</div>
<h2 class="abs headline h-fire" style="left:642px;top:1718px">Beyond<br>Ordinary</h2>
<p class="abs body-text" style="left:644px;top:1834px;width:380px">Imagine: Sipping cocktails by a sparkling pool, dancing the night away in a rooftop club with views that will blow your mind, indulging in flavors you've never tasted before, and scoring the perfect souvenir to brag about back home.</p>
<p class="abs body-text" style="left:644px;top:1970px;width:380px">This isn't just a vacation; it's a story you'll be telling for years to come.</p>
<div class="abs pill ghost" style="left:644px;top:2042px;width:120px;height:28px;justify-content:center">Learn more
  <svg viewBox="0 0 12 12"><path d="M2 6h8M7 3l3 3-3 3" stroke="currentColor" stroke-width="1.6" fill="none"/></svg></div>

<!-- outdoor -->
<div class="abs eyebrow" style="left:184px;top:2181px;width:160px">Outdoor Thrills</div>
<h2 class="abs headline h-surf" style="left:182px;top:2221px">Adventure<br>In the Sun</h2>
<p class="abs body-text" style="left:186px;top:2337px;width:370px">Dubai isn't just skyscrapers and deserts. It's a non-stop adventure waiting to happen. We're your insider guide to the coolest jet ski and wind surfing marinas, paragliding events, camel riding trips, and the most unforgettable experiences that are instagram-worthy.</p>
<div class="abs pill ghost" style="left:186px;top:2497px;width:120px;height:28px;justify-content:center">Learn more
  <svg viewBox="0 0 12 12"><path d="M2 6h8M7 3l3 3-3 3" stroke="currentColor" stroke-width="1.6" fill="none"/></svg></div>
<div class="photo" style="left:640px;top:2226px;width:414px;height:300px;background:var(--violet);transform:rotate(1.5deg)"></div>
<div class="photo" role="img" aria-label="Kitesurfer gliding over turquoise water" style="left:648px;top:2234px;width:400px;height:290px;background:linear-gradient(180deg,#6f9bd4,#3fb6d2 40%,#1d8fb4 70%,#d9eef2);transform:rotate(1deg)"></div>

<!-- more -->
<h2 class="abs headline h-more" style="left:0;top:2640px;width:1200px;text-align:center;font-size:56px;letter-spacing:6px">And so much more!</h2>
<div class="band abs"></div>
<div class="photo" role="img" aria-label="Shopper with bags on a phone call" style="left:187px;top:2741px;width:274px;height:404px;background:linear-gradient(180deg,#d8d4cf,#8c7a72 50%,#5a1f2a)">
  <div class="abs" style="left:0;bottom:0;width:100%;height:100%;background:var(--lime);clip-path:polygon(0 62%,100% 100%,0 100%)"></div>
  <div class="tile-tag">Discover<br>exclusive<br>deals</div></div>
<div class="photo" role="img" aria-label="Secluded pool among tropical plants" style="left:461px;top:2741px;width:278px;height:404px;background:linear-gradient(160deg,#2d4a28,#1fa6b5 50%,#2d3a24)">
  <div class="abs" style="left:0;bottom:0;width:100%;height:100%;background:#48e3a3;clip-path:polygon(0 62%,100% 100%,0 100%)"></div>
  <div class="tile-tag">Enjoy<br>secluded<br>staycations</div></div>
<div class="photo" role="img" aria-label="Crowded nightclub under purple lights" style="left:739px;top:2741px;width:281px;height:404px;background:linear-gradient(180deg,#3a1a6a,#c23ad8 40%,#5a1a8a 70%,#2a0f4a)">
  <div class="abs" style="left:0;bottom:0;width:100%;height:100%;background:#8a5af0;clip-path:polygon(0 62%,100% 100%,0 100%)"></div>
  <div class="tile-tag">Explore<br>Dubai's<br>nightlife</div></div>

<!-- contact -->
<h2 class="abs" style="left:186px;top:3264px;font-family:'Montserrat',sans-serif;font-weight:900;font-size:44px;line-height:42px;letter-spacing:5px">START YOUR<br>JOURNEY TODAY</h2>
<p class="abs" style="left:186px;top:3368px;font-weight:700;font-size:16.5px;color:var(--violet);letter-spacing:.5px">Ready to start your dream adventure?</p>
<p class="abs body-text" style="left:186px;top:3409px;width:370px;color:#fff">This isn't just a vacation; it's the story you'll be telling for years to come. Don't miss out on the ultimate Dubai adventure and an experience of a lifetime.</p>
<p class="abs contact-line" style="left:186px;top:3490px"><b>Phone:</b> (555) 204-1188</p>
<p class="abs contact-line" style="left:186px;top:3526px"><b>Email:</b> hello@sunvistadubai</p>
<p class="abs contact-line" style="left:186px;top:3560px"><b>Address:</b> 82 Harbor Crest Road, Marina Bay CA. 90210</p>
<form class="abs form-box">
  <div class="field" style="top:48px">Full Name *</div>
  <div class="field" style="top:106px">Email Address *</div>
  <div class="field" style="top:164px">Phone Number *</div>
  <div class="field" style="top:224px">Your Message *</div>
  <div class="abs pill solid" style="left:36px;top:282px;width:152px;height:34px;justify-content:center;background:var(--mint-bright);font-size:12px">Send
    <svg viewBox="0 0 12 12"><rect x="1" y="2.5" width="10" height="7" fill="none" stroke="#fff" stroke-width="1.3"/><path d="M1 2.5l5 4 5-4" fill="none" stroke="#fff" stroke-width="1.3"/></svg></div>
</form>

<!-- footer -->
<footer class="abs footer">
  <div class="abs brand" style="left:0;top:56px;width:1200px;text-align:center">Sunvista Dubai</div>
  <nav class="abs nav" style="left:0;top:157px;width:1200px">
    <a style="left:201px">Home</a>
    <a style="left:320px">UAE Life</a>
    <a style="left:471px">Emirates Insider</a>
    <a style="left:652px">Career Corner</a>
    <a style="left:826px">HR Essentials</a>
    <a style="left:983px">Blog Beat</a>
  </nav>
  <div class="abs" style="left:200px;top:253px;width:280px"><div class="foot-head">Visit us</div><p class="foot-text" style="margin-top:12px">82 Harbor Crest Road, Marina Bay<br>CA. 90210</p></div>
  <div class="abs" style="left:460px;top:253px;width:280px"><div class="foot-head">Contact us</div><p class="foot-text" style="margin-top:12px;color:#fff"><b>Phone:</b> (555) 204-1188<br><b>Email:</b> hello@sunvistadubai</p></div>
  <div class="abs" style="left:766px;top:253px;width:280px"><div class="foot-head">Never miss a beat</div>
    <div class="social" style="justify-content:center;margin-top:12px"><span style="width:32px;height:32px"></span><span style="width:32px;height:32px"></span><span style="width:32px;height:32px"></span></div></div>
</footer>

</body>
</html>
```